Es wurden alle Wünsche immer rasch und professionell umgesetzt. Wir sind rundum zufrieden. Vielen Dank :)
Wir sind ein junges Fotografen-Paar, und wollen heuer neu durchstarten mit Kinder- und Neugeborenen Fotografie. Unsere Zielgruppe sind vor allem schwangere Frauen, die frühzeitig ein Newborn-Shooting oder vorab ein Schwangerschafts-Shooting buchen möchten. Wir sind auf der Suche nach einem minimalistischen Flyer zum Auslegen in diversen Einrichtungen, und einer dazu passenden Visitenkarte.
Wir haben kein Logo, möchten aber auch nichts aufwendiges. Es darf auch ein passendes fertiges Stock-Logo sein.
Wir lieben den BoHo Stil, und fotografieren auch fast ausschließlich in diesem. Dementsprechend stellen wir uns unseren Flyer bzw unsere Visitenkarte minimalistisch vor. Da es um Kinder und Babys geht, ziehen wir die Farbe Altrosa/Rosé vor, eventuell als Akzentfarbe, oder auch als Hintergrundfarbe.
Der Flyer zum Auslegen in Tagesstätten oder zB im Krankenhaus stellen wir uns quadratisch vor (einfacher Flyer/Doppelseitig).
Die Visitenkarte eventuell Hochformat, jedoch sind wir hier total offen. Meine Partnerin meint ein 'BOHO-Regenbogen' wäre bestimmt sehr lieb, jedoch soll dies keine Voraussetzung sein.
Auf der Vorderseite soll unser Logo und ein Foto sein (Baby/Newborn).
Auf der Rückseite mindestens 3-4 unserer Bilder, und einen kurzen Text plus Kontaktdaten.

```html
<!DOCTYPE html>
<html lang="de">
<head>
<meta charset="utf-8">
<title>kleinwunder – Visitenkarte</title>
<link rel="stylesheet" href="https://fonts.googleapis.com/css2?family=Quicksand:wght@500;600;700&display=swap">
<style>
  :root {
    --mauve: #a57c7a;
    --peach: #d99c82;
    --peach-soft: #ecd5ca;
    --rose-soft: #d7bfbd;
    --cream: #f6efed;
    --ink: #454a52;
    --frame: #f1e3e0;
    --stage: #ffffff;
  }
  * { box-sizing: border-box; margin: 0; padding: 0; }
  html, body {
    width: 1200px; height: 927px; overflow: hidden;
    background: var(--stage);
    font-family: "Quicksand", sans-serif;
  }
  .canvas { position: relative; width: 1200px; height: 927px; }

  .card {
    position: absolute; top: 163px;
    width: 400px; height: 600px;
    box-shadow: 0 4px 14px rgba(0,0,0,.12);
    overflow: hidden;
  }

  /* back side */
  .card--back { left: 130px; background: var(--mauve); }
  .card--back .frame {
    position: absolute; inset: 14px;
    border: 1.5px solid var(--frame); opacity: .75;
    border-radius: 3px;
  }
  .brand {
    position: absolute; left: 0; right: 0;
    display: flex; flex-direction: column; align-items: center; gap: 18px;
  }
  .card--back .brand { top: 205px; }
  .brand-dot {
    width: 86px; height: 86px; border-radius: 50%;
    background: var(--peach-soft);
  }
  .brand-name {
    font-weight: 600; font-size: 30px; letter-spacing: 1px;
    color: var(--ink);
  }
  .card--back .brand-name { color: var(--cream); }
  .card--back .web {
    position: absolute; left: 0; right: 0; bottom: 44px;
    text-align: center; font-size: 13px; font-weight: 600;
    letter-spacing: 2.5px; color: var(--peach-soft);
  }

  /* front side */
  .card--front { left: 670px; background: var(--cream); }
  .card--front .frame {
    position: absolute; inset: 12px;
    border: 1px solid var(--rose-soft); opacity: .8;
  }
  .block { position: absolute; }
  .block--peach { right: 0; top: 60px; width: 150px; height: 190px; background: var(--peach-soft); opacity: .8; }
  .block--rose { left: 0; bottom: 24px; width: 120px; height: 150px; background: var(--rose-soft); opacity: .7; }

  .rainbow-area {
    position: absolute; width: 170px; height: 140px;
    background: linear-gradient(135deg, var(--mauve) 0%, var(--peach) 100%);
    opacity: .55;
  }
  .rainbow-area--top { left: 40px; top: 36px; }
  .rainbow-area--bottom { right: 36px; bottom: 36px; }

  .card--front .brand { top: 196px; gap: 10px; }
  .card--front .brand-dot { width: 56px; height: 56px; background: var(--peach); opacity: .55; }
  .card--front .brand-name { font-size: 26px; }

  .contacts {
    position: absolute; left: 0; right: 0; top: 312px;
    list-style: none; display: flex; flex-direction: column; align-items: center; gap: 12px;
  }
  .contact {
    display: flex; align-items: center; gap: 10px; width: 220px;
    font-size: 14px; font-weight: 700; color: var(--ink);
  }
  .contact-icon {
    width: 22px; height: 22px; border-radius: 50%;
    background: var(--ink); flex: none;
    display: flex; align-items: center; justify-content: center;
  }
</style>
</head>
<body>
<main class="canvas">

  <section class="card card--back" aria-label="Rückseite">
    <div class="frame"></div>
    <div class="brand">
      <span class="brand-dot"></span>
      <span class="brand-name">kleinwunder</span>
    </div>
    <p class="web">www.kleinwunder-foto.de</p>
  </section>

  <section class="card card--front" aria-label="Vorderseite">
    <div class="block block--peach"></div>
    <div class="block block--rose"></div>
    <div class="frame"></div>

    <div class="rainbow-area rainbow-area--top" role="img" aria-label="Boho-Regenbogen mit Herz in Altrosa und Pfirsich"></div>
    <div class="rainbow-area rainbow-area--bottom" role="img" aria-label="Boho-Regenbogen mit Herz in Altrosa und Pfirsich"></div>

    <div class="brand">
      <span class="brand-dot"></span>
      <span class="brand-name">kleinwunder</span>
    </div>

    <ul class="contacts">
      <li class="contact">
        <span class="contact-icon">
          <svg width="12" height="12" viewBox="0 0 24 24" aria-hidden="true"><path fill="#fff" d="M6.6 10.8a15.1 15.1 0 0 0 6.6 6.6l2.2-2.2a1 1 0 0 1 1-.25 11.4 11.4 0 0 0 3.6.57 1 1 0 0 1 1 1V20a1 1 0 0 1-1 1A17 17 0 0 1 3 4a1 1 0 0 1 1-1h3.5a1 1 0 0 1 1 1c0 1.25.2 2.45.57 3.57a1 1 0 0 1-.25 1z"/></svg>
        </span>
        0151 2468 1357
      </li>
      <li class="contact">
        <span class="contact-icon">
          <svg width="12" height="12" viewBox="0 0 24 24" aria-hidden="true"><rect x="3" y="6" width="18" height="12" rx="1.5" fill="none" stroke="#fff" stroke-width="2"/><path d="M3.5 7l8.5 6 8.5-6" fill="none" stroke="#fff" stroke-width="2"/></svg>
        </span>
        hallo@kleinwunder-foto.de
      </li>
      <li class="contact">
        <span class="contact-icon">
          <svg width="12" height="12" viewBox="0 0 24 24" aria-hidden="true"><circle cx="12" cy="12" r="9" fill="none" stroke="#fff" stroke-width="2"/><ellipse cx="12" cy="12" rx="4" ry="9" fill="none" stroke="#fff" stroke-width="2"/><path d="M3 12h18" stroke="#fff" stroke-width="2"/></svg>
        </span>
        www.kleinwunder-foto.de
      </li>
    </ul>
  </section>

</main>
</body>
</html>
```